Corporate Capability Brochure for LumoByte

Create Corporate Capability Brochure for Executive IT Consulting Firm. Minority Business Enterprise (MBE) and Service Disabled Veteran Owned Small Business (SDVOSB). LumoByte is an Executive Information Technology Consulting Firm. We specialize in combining people with technology to deliver the Business of IT. We partner with C-Level Executives and their organizations to leverage technology that drives innovation and accelerates business transformation and enable businesses, governments and educational institutions to operate more successfully in a world where everything is increasingly linked together.

Looking for something clean, professional, innovative, eye-catching and creates a strong presence. The final design should communicate our numerous service offerings.

We are in the processing of updating our website so please use information obtained from capability statement uploaded. PLEASE USE LUMOBYTE CAPABILITY STATEMENT-COMMERCIAL (FILE 1) for content to be used in flyer/brochure being requested. Presentation was uploaded as a document to gauge style. We are still in the process of finding our style when it comes to marketing materials. Creativity is highly welcomed.

Target Market(s)

C-Level Executives. We work with Education Institutions, Healthcare Agencies, Federal Government Clients, Sports and Entertainment Companies and Technology companies.

Industry/Entity Type

Information Technology

Requirements
Should not have
• No Dark Backgrounds that make it hard to see
• No playful fonts that come across unprofessional
• Would prefer not to have images of people-Unless image provides Diversity

```html
<!DOCTYPE html>
<html lang="en">
<head>
<meta charset="utf-8">
<title>LumoByte Capability Brochure</title>
<link rel="stylesheet" href="https://fonts.googleapis.com/css2?family=Montserrat:wght@400;500;600&family=PT+Sans:wght@400;700&display=swap">
<style>
:root{
  --red:#c8171e;
  --red-dark:#8f0f14;
  --ink:#222;
  --charcoal:#444546;
  --paper:#fff;
  --backdrop:#e9e9ea;
  --box-fill:#f5f5f5;
}
*{box-sizing:border-box;margin:0;padding:0}
html,body{width:1200px;height:1200px;overflow:hidden;background:var(--backdrop)}
body{font-family:"PT Sans",Arial,sans-serif;color:var(--ink)}
.brochure{position:absolute;left:187px;top:20px;width:826px;height:1160px;background:var(--paper);overflow:hidden;box-shadow:0 2px 10px rgba(0,0,0,.15)}
.masthead{position:absolute;left:0;top:0;width:100%;height:214px;background:linear-gradient(100deg,#b5141a 0%,#d52a2f 45%,#c21a20 70%,#e0484b 100%)}
.brand{position:absolute;top:40px;left:0;width:100%;display:flex;justify-content:center;align-items:center;gap:12px}
.brand-mark{width:44px;height:44px;border:3px solid #fff}
.brand-name{font-family:"Montserrat",sans-serif;font-weight:400;font-size:40px;color:#fff;letter-spacing:2px}
.contact{position:absolute;left:226px;top:108px;list-style:none;font-family:"Montserrat",sans-serif;font-weight:500;font-size:15px;color:#fff}
.contact li{display:flex;align-items:center;gap:9px;height:24px}
.contact svg{width:17px;height:17px;flex:none}
.contact .social span+svg{margin-left:28px}
.rule{position:absolute;top:214px;left:0;width:100%;height:11px;background:var(--charcoal)}
.section-title{font-family:"Montserrat",sans-serif;font-weight:500;font-size:26px;color:var(--red);display:flex;align-items:center;gap:8px;margin-bottom:14px}
.section-title svg{width:28px;height:28px}
.about{position:absolute;left:22px;top:240px;width:272px;font-size:10.6px;line-height:1.36;text-align:justify}
.about p+p{margin-top:7px}
.divider{position:absolute;left:297px;top:252px;width:1px;height:290px;background:#333}
.advantage{position:absolute;left:312px;top:240px;width:500px;font-size:10.6px;line-height:1.36}
.values{list-style:none;margin:6px 0 6px}
.values li{position:relative;padding-left:24px;margin-bottom:6px}
.values svg{position:absolute;left:4px;top:3px;width:10px;height:10px}
.values strong{font-family:"Montserrat",sans-serif;font-weight:500;font-size:11px;display:block}
.services{position:absolute;left:29px;top:574px;width:770px;height:354px;border:1.5px solid var(--red);border-radius:22px;background:var(--box-fill);padding:42px 22px 0}
.services-title{position:absolute;left:50%;top:-22px;transform:translateX(-50%);width:256px;height:44px;border-radius:22px;background:var(--red);color:#fff;font-family:"Montserrat",sans-serif;font-weight:500;font-size:27px;display:flex;align-items:center;justify-content:center}
.services-intro{font-size:11px;line-height:1.34;margin-bottom:14px}
.service-grid{display:grid;width:100%;grid-template-columns:1.12fr 1fr 1.08fr 0.95fr;column-gap:20px;font-size:9.6px;line-height:1.36;text-align:justify}
.service{min-width:0}
.service h3{font-family:"PT Sans",sans-serif;font-weight:400;font-size:12px;color:var(--red);line-height:1.2;text-align:left}
.service h4{font-weight:400;font-size:12px;margin-top:11px;text-align:left}
.skyline{position:absolute;left:0;top:932px;width:100%;height:148px;background:linear-gradient(180deg,#fff 0%,#b8c8d8 18%,#5c7590 50%,#3b4a5c 80%,#2d3744 100%)}
.footer{position:absolute;left:0;top:1080px;width:100%;height:80px;background:var(--charcoal);display:flex;align-items:center;justify-content:center;font-family:"Montserrat",sans-serif;font-weight:400;font-size:19px;letter-spacing:13px;color:#fff}
</style>
</head>
<body>
<main class="brochure">
  <header class="masthead" role="img" aria-label="Red-tinted photograph of server racks in a data centre">
    <div class="brand"><span class="brand-mark"></span><span class="brand-name">LUMOBYTE</span></div>
    <ul class="contact">
      <li><svg viewBox="0 0 20 20"><circle cx="10" cy="10" r="9" fill="none" stroke="#fff" stroke-width="1.5"/><path d="M10 15s-4-4-4-7a4 4 0 0 1 8 0c0 3-4 7-4 7z" fill="#fff"/></svg>210 Harbor Street Suite 900 Lakeview, NY 14000</li>
      <li><svg viewBox="0 0 20 20"><circle cx="10" cy="10" r="9" fill="none" stroke="#fff" stroke-width="1.5"/><path d="M7 5l2 2-1 2 3 3 2-1 2 2-2 2c-4 0-8-4-8-8z" fill="#fff"/></svg>(555) 014-2290</li>
      <li><svg viewBox="0 0 20 20"><circle cx="10" cy="10" r="9" fill="none" stroke="#fff" stroke-width="1.5"/><rect x="5" y="7" width="10" height="7" fill="#fff"/><path d="M5 7l5 4 5-4" stroke="#c8171e" fill="none"/></svg>readytoinnovate@lumobyte.com</li>
      <li class="social"><svg viewBox="0 0 20 20"><circle cx="10" cy="10" r="9" fill="none" stroke="#fff" stroke-width="1.5"/></svg><span>lumobyte</span><svg viewBox="0 0 20 20"><circle cx="10" cy="10" r="9" fill="#fff"/></svg><span>@lumobyte</span></li>
    </ul>
  </header>
  <div class="rule"></div>

  <section class="about">
    <h2 class="section-title"><svg viewBox="0 0 28 28"><circle cx="14" cy="14" r="12.5" fill="none" stroke="#c8171e" stroke-width="2"/><circle cx="14" cy="11" r="3" fill="#c8171e"/><path d="M9 20a5 5 0 0 1 10 0z" fill="#c8171e"/></svg>About Us</h2>
    <p>LumoByte is an Executive Information Technology Consulting Firm. We specialize in combining people with technology to deliver the Business of IT. We partner with C-Level Executives and their organizations to leverage technology that drives innovation and accelerates business transformation and enable businesses, governments and educational institutions to operate more successfully in a world where everything is increasingly linked together.</p>
    <p>From workshops to full IT assessments, from technology installations and upgrades to major architecture design and implementation, our unique approach, depth and breadth of offerings, and exceptional team help organizations everywhere understand how their IT services can be optimized and leveraged to their strategic advantage.</p>
  </section>
  <div class="divider"></div>

  <section class="advantage">
    <h2 class="section-title"><svg viewBox="0 0 28 28"><circle cx="14" cy="14" r="12.5" fill="none" stroke="#c8171e" stroke-width="2"/><path d="M6 14l4-3 4 2 4-2 4 3-5 4h-6z" fill="#c8171e"/></svg>The LUMOBYTE Advantage</h2>
    <p>LumoByte is well-known and respected for our innovation and for putting our clients first. We are committed to four essential values:</p>
    <ul class="values">
      <li><svg viewBox="0 0 10 10"><rect x=".5" y=".5" width="9" height="9" fill="none" stroke="#c8171e"/><path d="M2 5l2 2 4-4" stroke="#c8171e" fill="none" stroke-width="1.3"/></svg><strong>Leading with perspective as your trusted advisor</strong>we move the industry forward with our unique insights, points of view, ideas and solutions, leading our clients, partners and each other to think beyond the ordinary.</li>
      <li><svg viewBox="0 0 10 10"><rect x=".5" y=".5" width="9" height="9" fill="none" stroke="#c8171e"/><path d="M2 5l2 2 4-4" stroke="#c8171e" fill="none" stroke-width="1.3"/></svg><strong>Delivering real impact as your solver</strong>We dig hard into your problem and evaluate the bigger picture, then unite the optimal people, technology and know-how to execute the most effective solution.</li>
      <li><svg viewBox="0 0 10 10"><rect x=".5" y=".5" width="9" height="9" fill="none" stroke="#c8171e"/><path d="M2 5l2 2 4-4" stroke="#c8171e" fill="none" stroke-width="1.3"/></svg><strong>Working in the trenches as your partner</strong>we work shoulder to shoulder with you, understanding your needs as a team member, and acting in the belief that your success is ours.</li>
      <li><svg viewBox="0 0 10 10"><rect x=".5" y=".5" width="9" height="9" fill="none" stroke="#c8171e"/><path d="M2 5l2 2 4-4" stroke="#c8171e" fill="none" stroke-width="1.3"/></svg><strong>Unlocking tomorrow as your innovator</strong>we are relentlessly focused on fostering up great strategies, architecting great solutions, and designing for innovation by allowing our clients to see their IT challenges through a different lens.</li>
    </ul>
    <p>At LumoByte, our mission is to become your trusted advisor.</p>
  </section>

  <section class="services">
    <h2 class="services-title">Our Services</h2>
    <p class="services-intro">LumoByte's passion for the Business of IT and our commitment to quality results means we focus on the right solutions to meet your specific needs. Our focus on understanding, quantifying and measuring business results is a unique differentiator that allows us to deliver high-value, high-touch solutions with proven ROI. Our suite of services includes:</p>
    <div class="service-grid">
      <article class="service">
        <h3>Solutions-as-a-Service</h3>
        <p>We provide end-to-end solutions, utilizing consulting methodologies that are refined by decades of experience, across multiple disciplines. Whether you are addressing network, compute, data protection, virtualization or security, we provide the resources and expertise that allow your company to reach its goals.</p>
        <h4>Related Services:</h4>
        <p>Data Center Infrastructure, Data Center Facility Selection, Design and Build, Data Center Migration, Business Continuity and Disaster Recovery, Converged Infrastructure, Collaboration &amp; Mobility, External Infrastructure Strategy &amp; Selection.</p>
      </article>
      <article class="service">
        <h3>C-Suite-as-a-Service</h3>
        <p>We let you run your business while we help you plan, develop, evaluate, manage &amp; co-ordinate technology centric solutions.</p>
        <h4>Related Services:</h4>
        <p>Strategy Assessments, Executive Advising, CTO/CIO On Demand, Virtual CTO/CIO</p>
      </article>
      <article class="service">
        <h3>Technology Business Management (TBM)-as-a-Service</h3>
        <p>We help clients navigate the changing landscape at the intersection of Business and Technology enabling them to improve the way they make technology decisions. This allows them to optimize costs, quality and the overall value of their IT services.</p>
        <h4>Related Services:</h4>
        <p>Cloud Migration Programs, Cloud Strategy Roadmap Planning, Data Center &amp; Vendor Consolidation, Application Rationalization, Infrastructure Technology Assessment, IT Organization Change Management, IT Budget and Forecasting Process, Infrastructure Cost Savings Assessment</p>
      </article>
      <article class="service">
        <h3>Managed Security Services</h3>
        <p>Let us serve as a remote extension of your team to strengthen your security response and defenses.</p>
        <h4>Related Services:</h4>
        <p>Security Intelligence Including Co-Managed On-Premise SIEM, Hosted Multi-Tenant SIEM, Use Case Development and Best Practices, Monitoring and Notification, Log Management, Event Archiving, Platform, Vulnerability and Endpoint Management, Malware Remediation</p>
      </article>
    </div>
  </section>

  <div class="skyline" role="img" aria-label="Aerial photograph of a city skyline at dusk"></div>
  <footer class="footer">WWW.LUMOBYTE.COM</footer>
</main>
</body>
</html>
```